Web Design Project

The client is unsure if they want a completely new design or a design that matches their existing site closely (https://www.talvoinsurance.com.au). So essentially we are looking for some designs that reflect the existing sites shape and colour and some designs that have their own new style. The company will sell three main types of insurance, Car, Bike and Caravan.

Read the complete brief and in the attached document.
The logo is also attached

I have also attached a zip of a few classic cars, if you can incorporate those.

Industry/Entity Type

Insurance

Requirements
Should not have

```html
<!DOCTYPE html>
<html lang="en">
<head>
<meta charset="utf-8">
<title>Talvo Insurance</title>
<link rel="stylesheet" href="https://fonts.googleapis.com/css2?family=Montserrat:wght@400;700&family=Open+Sans:wght@400;600;700&family=Satisfy&display=swap">
<style>
:root{
  --dark:#2a2a2c;
  --nav:#1f1d1c;
  --blue:#3b8fcc;
  --blue-dark:#2b78b5;
  --blue-deep:#1f6aa5;
  --orange:#e8411c;
  --orange-dark:#b32d0e;
  --grey-bg:#f1f1f1;
  --grey-pattern:#e6e6e6;
  --text:#333;
  --muted:#555;
  --navy:#1d3b52;
  --white:#fff;
}
*{box-sizing:border-box;margin:0;padding:0}
html,body{width:1200px;height:2203px;overflow:hidden}
body{font-family:"Open Sans",Arial,sans-serif;color:var(--text);background:var(--white);position:relative}
.wrap{width:900px;margin:0 auto;position:relative}

/* header */
.topbar{height:81px;background:var(--dark)}
.topbar .wrap{height:81px}
.brand{position:absolute;left:0;top:14px;display:flex;align-items:center;gap:10px;font-family:"Montserrat",sans-serif;font-weight:700;font-size:20px;color:var(--white);letter-spacing:1px}
.brand-mark{width:22px;height:22px;border-radius:50%;background:var(--white)}
.contact-line{position:absolute;right:0;top:8px;font-family:"Montserrat",sans-serif;font-weight:700;font-size:13px;color:var(--white);letter-spacing:1px}
.contact-line b{font-size:17px;letter-spacing:2px;margin-left:4px}
.social{position:absolute;right:0;top:40px;display:flex;gap:5px}
.social span{width:25px;height:25px;background:#5a6b80;border-radius:3px}

.mainnav{height:41px;background:var(--nav)}
.mainnav .wrap{display:flex;align-items:center;height:41px}
.mainnav a{font-size:13px;color:var(--white);text-decoration:none;margin-right:28px;letter-spacing:.3px}
.mainnav a.active{color:var(--orange)}
.pay{margin-left:auto;display:flex;align-items:center;gap:10px;color:#4ea3e0;font-size:13px;letter-spacing:.3px}

/* hero */
.hero{position:relative;height:519px;background:linear-gradient(180deg,#c6a581 0%,#b88f63 30%,#8a7462 55%,#6e6255 100%);text-align:center}
.hero-visual{position:absolute;left:0;right:0;bottom:0;height:340px;background:linear-gradient(180deg,rgba(150,130,110,0) 0%,rgba(95,85,75,.6) 100%)}
.hero h1{position:relative;padding-top:22px;font-family:"Montserrat",sans-serif;font-weight:700;font-size:36px;line-height:42px;color:var(--white);letter-spacing:1px}
.hero-cta{position:relative;display:flex;justify-content:center;align-items:center;gap:12px;margin-top:12px;margin-left:60px}
.script{font-family:"Satisfy",cursive;font-size:21px;color:#222}
.btn-quote{display:inline-block;background:var(--orange);color:var(--white);font-weight:700;font-size:18px;padding:9px 34px;border-radius:2px;box-shadow:inset 0 -3px 0 var(--orange-dark)}

/* welcome */
.welcome{height:154px;background:var(--blue)}
.welcome .wrap{display:flex;padding-top:24px}
.welcome h2{width:222px;font-family:"Montserrat",sans-serif;font-weight:700;font-size:27px;line-height:33px;color:#1d4f78}
.welcome p{flex:1;font-size:10px;line-height:17px;color:#1d4f78}
.btn{display:inline-block;background:var(--orange);color:var(--white);font-weight:700;font-size:11px;padding:6px 11px;border:1px solid var(--orange-dark);border-radius:2px;letter-spacing:.3px}
.welcome .btn{position:absolute;left:222px;top:106px}

/* products */
.products{height:429px;background:var(--grey-bg)}
.products .wrap{display:flex;justify-content:space-between;padding-top:27px}
.product{width:285px}
.product-img{height:93px;width:200px;margin:0 0 0 20px;border-radius:40px;background:linear-gradient(180deg,#e6e6e6,#bdbdbd)}
.product h3{margin-top:35px;font-family:"Montserrat",sans-serif;font-size:20px;font-weight:400;color:#222}
.product h3 b{font-weight:700}
.product p{margin-top:16px;font-size:11px;line-height:16.5px;color:var(--muted)}
.product .btn{margin-top:22px}

/* section tabs */
.tab{position:absolute;left:0;height:55px;background:var(--blue);padding-left:150px;display:flex;align-items:center;font-family:"Montserrat",sans-serif;font-weight:700;font-size:22px;color:var(--white);letter-spacing:.5px}
.tab::after{content:"";position:absolute;right:-14px;top:0;border-left:14px solid var(--blue-deep);border-top:9px solid transparent}

.benefits{position:relative;height:271px;background:var(--grey-pattern)}
.benefits .tab{top:2px;width:424px}
.benefit-grid{position:absolute;left:150px;top:96px;width:900px;display:grid;grid-template-columns:316px 308px 276px;row-gap:22px}
.benefit{display:flex;gap:18px;font-size:13px;line-height:19px;color:#333}
.benefit svg{flex:none}

.events{position:relative;height:276px;background:var(--white)}
.events .tab{top:2px;width:384px}
.event-row{position:absolute;left:150px;top:98px;width:900px;display:flex;justify-content:space-between}
.event{position:relative;width:285px;height:134px;background:linear-gradient(135deg,#8a5d4a,#4a4648 50%,#a88f63)}
.event-bar{position:absolute;left:0;right:0;bottom:0;height:38px;background:rgba(0,0,0,.55);display:flex;justify-content:space-between;padding:5px 17px 0;color:var(--white);font-size:11px;font-weight:700;line-height:13px}
.event-bar .title{width:120px;text-decoration:underline}

.partners{position:relative;height:149px;background:var(--grey-bg)}
.partners .tab{top:0;width:290px}
.partner-row{position:absolute;left:150px;top:86px;width:900px;display:flex;justify-content:space-between;align-items:center}
.partner-row span{display:block;background:#3a3a3a;height:30px}

.cta-band{height:155px;background:var(--blue)}
.cta-band .wrap{display:flex;align-items:center;height:155px}
.cta-band h2{width:500px;font-family:"Montserrat",sans-serif;font-weight:700;font-size:27px;line-height:29px;color:var(--white);text-align:center;margin-left:-5px}
.cta-side{margin-left:40px;position:relative;height:100px;width:370px}
.cta-side .btn-quote{position:absolute;left:0;top:10px;font-size:18px;padding:10px 34px}
.cta-side .script{position:absolute;left:82px;top:66px;color:#1a2f45}

.footer{height:128px;background:var(--navy);text-align:center;padding-top:25px}
.footer nav a{font-size:11px;color:var(--white);text-decoration:none;margin:0 11px}
.footer address{font-style:normal;margin-top:12px;font-size:11px;line-height:16px;color:#3f95d6}
.footer small{display:block;margin-top:10px;font-size:11px;color:var(--white)}
</style>
</head>
<body>

<header class="topbar">
  <div class="wrap">
    <div class="brand"><span class="brand-mark"></span>TALVO INSURANCE</div>
    <div class="contact-line">QUESTIONS / CALL US : <b>123 - 456 - 789 - 0</b></div>
    <div class="social"><span></span><span></span><span></span><span></span></div>
  </div>
</header>
<nav class="mainnav">
  <div class="wrap">
    <a class="active" href="#">HOME</a><a href="#">ABOUT US</a><a href="#">INSURANCE</a><a href="#">EVENTS</a><a href="#">CLUBS</a><a href="#">LINKS</a><a href="#">FAQ</a><a href="#">CONTACT US</a>
    <span class="pay">MAKE A PAYMENT
      <svg width="18" height="18" viewBox="0 0 18 18"><circle cx="9" cy="9" r="9" fill="#4ea3e0"/><path d="M9 4l-4 5h3v5h2V9h3z" fill="#fff"/></svg>
    </span>
  </div>
</nav>

<section class="hero">
  <div class="hero-visual" role="img" aria-label="Motorhome, red sedan and motorcycle parked on a desert plain below mountains"></div>
  <h1>GET THE BEST DEAL ON YOUR<br>CAR, BIKE AND CARAVAN INSURANCE</h1>
  <div class="hero-cta">
    <span class="script">Find out how much you can save</span>
    <span class="btn-quote">INSTANT QUOTE</span>
  </div>
</section>

<section class="welcome">
  <div class="wrap">
    <h2>WELCOME TO INSURANCE</h2>
    <p>Donec magna nibh, convallis et dapibus at, suscipit ut augue. Phasellus eleifend pulvinar facilisis. Donec risus lorem, accumsan sed molestie ut, consequat in tellus. Sed suscipit nulla tincidunt augue consectetur blandit ullam corper velit sagittis. Lorem ipsum dolor sit amet, consectetur adipiscing elit. Ut a dolor nisi. Ut fermentum semper orci, ut pretium nibh hendrerit ac.</p>
    <span class="btn">LEARN MORE</span>
  </div>
</section>

<section class="products">
  <div class="wrap">
    <article class="product">
      <div class="product-img" role="img" aria-label="Silver sedan car"></div>
      <h3><b>CAR</b> INSURANCE</h3>
      <p>Lorem ipsum dolor sit amet, consectetur adipiscing elit. Ut luctus diam a diam condimentum vitae vulputate lacus congue.</p>
      <p>Donec sed erat sed orci luctus interdum quis id erat. Mauris eleifend tincidunt tincidunt. Morbi non tortor malesuada lorem mattis interdum. Nulla facilisi. Sed sed porta lorem. Ut in turpis nisi.</p>
      <span class="btn">LEARN MORE</span>
    </article>
    <article class="product">
      <div class="product-img" role="img" aria-label="Sport motorbike"></div>
      <h3><b>BIKE</b> INSURANCE</h3>
      <p>Lorem ipsum dolor sit amet, consectetur adipiscing elit. Ut luctus diam a diam condimentum vitae vulputate lacus congue.</p>
      <p>Donec sed erat sed orci luctus interdum quis id erat. Mauris eleifend tincidunt tincidunt. Morbi non tortor malesuada lorem mattis interdum. Nulla facilisi. Sed sed porta lorem. Ut in turpis nisi.</p>
      <span class="btn">LEARN MORE</span>
    </article>
    <article class="product">
      <div class="product-img" role="img" aria-label="Small teardrop caravan"></div>
      <h3><b>CARAVAN</b> INSURANCE</h3>
      <p>Lorem ipsum dolor sit amet, consectetur adipiscing elit. Ut luctus diam a diam condimentum vitae vulputate lacus congue.</p>
      <p>Donec sed erat sed orci luctus interdum quis id erat. Mauris eleifend tincidunt tincidunt. Morbi non tortor malesuada lorem mattis interdum. Nulla facilisi. Sed sed porta lorem. Ut in turpis nisi.</p>
      <span class="btn">LEARN MORE</span>
    </article>
  </div>
</section>

<svg width="0" height="0" style="position:absolute">
  <symbol id="tick" viewBox="0 0 24 24"><circle cx="12" cy="12" r="10.5" fill="none" stroke="#e8411c" stroke-width="2"/><path d="M7 12.5l3.5 3.5L17 9" fill="none" stroke="#e8411c" stroke-width="2"/></symbol>
</svg>

<section class="benefits">
  <h2 class="tab">OUR POLICY BENEFITS</h2>
  <div class="benefit-grid">
    <div class="benefit"><svg width="24" height="24"><use href="#tick"/></svg>Agreed Value</div>
    <div class="benefit"><svg width="24" height="24"><use href="#tick"/></svg>Lifetime Guarantee for Repairs</div>
    <div class="benefit"><svg width="24" height="24"><use href="#tick"/></svg>Flexible coverage</div>
    <div class="benefit"><svg width="24" height="24"><use href="#tick"/></svg>New Replacement Vehicle in first<br>2 years</div>
    <div class="benefit"><svg width="24" height="24"><use href="#tick"/></svg>Free Windscreen/Glass Benefit</div>
    <div class="benefit"><svg width="24" height="24"><use href="#tick"/></svg>Pay Premiums by Instalments</div>
    <div class="benefit"><svg width="24" height="24"><use href="#tick"/></svg>Choice of Repairer</div>
    <div class="benefit"><svg width="24" height="24"><use href="#tick"/></svg>Hire car following accident or theft</div>
    <div class="benefit"><svg width="24" height="24"><use href="#tick"/></svg>Salvage retained by you on vehicles<br>over 30 years</div>
  </div>
</section>

<section class="events">
  <h2 class="tab">UPCOMING EVENTS</h2>
  <div class="event-row">
    <article class="event" role="img" aria-label="Cars on display at a motor show">
      <div class="event-bar"><span>08<br>JAN 2013</span><span class="title">LOREM IPSUM DOLOR SIT AMET,</span></div>
    </article>
    <article class="event" role="img" aria-label="Motorbikes on stage at an expo">
      <div class="event-bar"><span>08<br>JAN 2013</span><span class="title">LOREM IPSUM DOLOR SIT AMET,</span></div>
    </article>
    <article class="event" role="img" aria-label="Classic vans at an exhibition hall">
      <div class="event-bar"><span>08<br>JAN 2013</span><span class="title">LOREM IPSUM DOLOR SIT AMET,</span></div>
    </article>
  </div>
</section>

<section class="partners">
  <h2 class="tab">PARTNERS</h2>
  <div class="partner-row">
    <span style="width:110px;height:24px"></span>
    <span style="width:100px;height:40px"></span>
    <span style="width:150px;height:28px"></span>
    <span style="width:78px;height:44px"></span>
    <span style="width:130px;height:40px"></span>
    <span style="width:62px;height:42px"></span>
  </div>
</section>

<section class="cta-band">
  <div class="wrap">
    <h2>GET THE BEST DEAL ON YOUR CAR, BIKE AND CARAVAN INSURANCE</h2>
    <div class="cta-side">
      <span class="btn-quote">INSTANT QUOTE</span>
      <svg style="position:absolute;left:232px;top:14px" width="60" height="48" viewBox="0 0 60 48"><path d="M54 44C50 22 34 12 10 14" fill="none" stroke="#1a2f45" stroke-width="3"/><path d="M18 5L6 14l12 8" fill="none" stroke="#1a2f45" stroke-width="3"/></svg>
      <span class="script">Find out how much you can save</span>
    </div>
  </div>
</section>

<footer class="footer">
  <nav><a href="#">HOME</a><a href="#">ABOUT US</a><a href="#">INSURANCE</a><a href="#">EVENTS</a><a href="#">CLUBS</a><a href="#">LINKS</a><a href="#">FAQ</a><a href="#">CONTACT US</a></nav>
  <address>Talvo Insurance Services 27 Wattlebank Road Greenfield Qld 4110<br>Ph: 1300 000 111 &nbsp;|&nbsp; Fx: 1300 000 222 &nbsp;|&nbsp; admin@talvoinsurance.com.au</address>
  <small>Copyright © 2012 Brightline Studio. All Rights Reserved</small>
</footer>

</body>
</html>
```